Real Estate Business Cards

Looking for a clean, sharp and professional look for our Real Estate investment Fund that invests in Multi Family Apartment buildings.

Target Market(s)

Real Estate Fund

Industry/Entity Type

Real Estate

Contact Information for Business Card

Company Description: Real Estate Investment Fund
Company Name: RKW Holdings
Name: Marcus Olvane
Cell: (917) 482-0657
Email: marcus@rkwholdings-example.com
Website: www.rkwholdings-example.com
Address: 418, 9th Street, Brooklyn NY 11218

Colors

Designer to choose colors to be used in the design.

Requirements
Nice to have
• Colors to match logo

```html
<!DOCTYPE html>
<html lang="en">
<head>
<meta charset="utf-8">
<title>RKW Holdings – Business Cards</title>
<link rel="stylesheet" href="https://fonts.googleapis.com/css2?family=Cormorant+Garamond:wght@500&family=Open+Sans:wght@400;600&display=swap">
<style>
  :root {
    --page-bg: #d4d4d4;
    --brand-blue: #146ca3;
    --brand-blue-deep: #0f5a8a;
    --paper: #ffffff;
    --paper-shade: #ececec;
    --ink: #3a3a3a;
    --ink-soft: #5a5a5a;
    --rule: #8c8c8c;
    --light-mark: #e3e5e8;
  }
  * { box-sizing: border-box; margin: 0; padding: 0; }
  html, body { width: 1200px; height: 900px; overflow: hidden; }
  body {
    background: var(--page-bg);
    display: flex;
    flex-direction: column;
    align-items: center;
    justify-content: center;
    gap: 40px;
    font-family: "Open Sans", Arial, sans-serif;
  }
  .card {
    position: relative;
    width: 640px;
    height: 366px;
    overflow: hidden;
    box-shadow: 0 6px 14px rgba(0,0,0,0.25);
  }

  /* Front */
  .card-front {
    background: linear-gradient(160deg, var(--brand-blue-deep), var(--brand-blue) 55%);
    color: var(--paper);
  }
  .front-block {
    position: absolute;
    top: -20px;
    right: 70px;
    width: 190px;
    height: 190px;
    background: var(--light-mark);
    border-radius: 8px;
  }
  .front-identity {
    position: absolute;
    left: 44px;
    bottom: 46px;
  }
  .front-name {
    font-family: "Cormorant Garamond", Georgia, serif;
    font-weight: 500;
    font-size: 40px;
    letter-spacing: 1px;
    text-transform: uppercase;
    line-height: 1;
  }
  .front-tagline {
    margin-top: 8px;
    font-size: 15px;
    letter-spacing: 2.5px;
  }

  /* Back */
  .card-back {
    background: linear-gradient(180deg, var(--paper-shade), var(--paper) 45%);
    color: var(--ink);
  }
  .back-brand {
    position: absolute;
    left: 44px;
    top: 86px;
    display: flex;
    flex-direction: column;
    align-items: flex-start;
    gap: 14px;
  }
  .brand-square {
    width: 40px;
    height: 40px;
    background: var(--brand-blue);
  }
  .back-name {
    font-family: "Cormorant Garamond", Georgia, serif;
    font-weight: 500;
    font-size: 30px;
    letter-spacing: 1px;
    text-transform: uppercase;
    color: var(--brand-blue);
    line-height: 1;
  }
  .person {
    position: absolute;
    left: 44px;
    bottom: 48px;
  }
  .person-name {
    font-weight: 600;
    font-size: 21px;
    color: var(--brand-blue);
    text-transform: uppercase;
    line-height: 1.1;
  }
  .person-role {
    font-size: 15px;
    color: var(--ink-soft);
    text-transform: uppercase;
  }
  .contact {
    position: absolute;
    right: 36px;
    top: 70px;
    padding: 4px 0 4px 22px;
    border-left: 1.5px solid var(--rule);
    font-size: 13px;
    line-height: 1.55;
  }
  .contact-address { margin-bottom: 6px; }
  .contact-line {
    display: flex;
    align-items: center;
    gap: 8px;
  }
  .contact-line svg { width: 13px; height: 13px; flex: none; }
</style>
</head>
<body>

  <section class="card card-front">
    <div class="front-block" aria-hidden="true"></div>
    <div class="front-identity">
      <p class="front-name">RKW Holdings</p>
      <p class="front-tagline">Real Estate Investment Fund</p>
    </div>
  </section>

  <section class="card card-back">
    <div class="back-brand">
      <span class="brand-square" aria-hidden="true"></span>
      <p class="back-name">RKW Holdings</p>
    </div>

    <div class="person">
      <p class="person-name">Marcus Olvane</p>
      <p class="person-role">Realtor</p>
    </div>

    <div class="contact">
      <p class="contact-address">418, 9th Street<br>Brooklyn NY 11218</p>
      <p class="contact-line">
        <svg viewBox="0 0 14 14" aria-hidden="true"><rect x="3" y="1" width="8" height="12" rx="1.5" fill="none" stroke="#146ca3" stroke-width="1.4"/><line x1="6" y1="11" x2="8" y2="11" stroke="#146ca3" stroke-width="1.2"/></svg>
        (917) 482-0657
      </p>
      <p class="contact-line">
        <svg viewBox="0 0 14 14" aria-hidden="true"><rect x="1" y="3" width="12" height="8" fill="none" stroke="#146ca3" stroke-width="1.4"/><polyline points="1,3 7,8 13,3" fill="none" stroke="#146ca3" stroke-width="1.2"/></svg>
        marcus@rkwholdings-example.com
      </p>
      <p class="contact-line">
        <svg viewBox="0 0 14 14" aria-hidden="true"><circle cx="7" cy="7" r="5.8" fill="none" stroke="#146ca3" stroke-width="1.3"/><ellipse cx="7" cy="7" rx="2.5" ry="5.8" fill="none" stroke="#146ca3" stroke-width="1"/><line x1="1.2" y1="7" x2="12.8" y2="7" stroke="#146ca3" stroke-width="1"/></svg>
        www.rkwholdings-example.com
      </p>
    </div>
  </section>

</body>
</html>
```